Building Company Business Card Design

I am looking to get a business card designed for my Building Company. Please find the logo attached.

Industry/Entity Type

Business

Contact Information for Business Card

Mobile 0472 913 046
Email admin@tarrowconstructworks.com.au
Website www.tarrowconstructworks.com.au

Colors
0255a3

```html
<!DOCTYPE html>
<html lang="en">
<head>
<meta charset="UTF-8">
<title>Tarrow Construct Works – Business Card</title>
<link rel="stylesheet" href="https://fonts.googleapis.com/css2?family=Montserrat:wght@700&family=Lato:wght@300;400&display=swap">
<style>
  :root {
    --brand-blue: #0255a3;
    --brand-blue-light: #1a72c4;
    --brand-blue-dark: #014a8f;
    --paper: #ffffff;
    --paper-shade: #e6e6e8;
    --ink-grey: #5c5f66;
    --stage: #2b2b2d;
  }
  * { box-sizing: border-box; margin: 0; padding: 0; }
  html, body {
    width: 1200px; height: 1031px; overflow: hidden;
    background: var(--stage);
  }
  .canvas {
    position: relative; width: 1200px; height: 1031px;
  }
  .card {
    position: absolute; left: 290px;
    width: 620px; height: 360px;
    border-radius: 22px; overflow: hidden;
    box-shadow: 0 18px 40px rgba(0,0,0,.45);
  }
  /* Front */
  .card-front {
    top: 110px;
    background: linear-gradient(135deg, var(--brand-blue-light) 0%, var(--brand-blue) 55%, var(--brand-blue-dark) 100%);
    color: var(--paper);
  }
  .front-wordmark {
    position: absolute; left: 0; right: 0; top: 130px;
    display: flex; align-items: center; justify-content: center; gap: 14px;
  }
  .wordmark-dot {
    width: 16px; height: 16px; border-radius: 50%;
    background: currentColor;
  }
  .wordmark-name {
    font-family: "Montserrat", sans-serif; font-weight: 700;
    font-size: 34px; letter-spacing: 1px; text-transform: uppercase;
  }
  .front-web {
    position: absolute; left: 0; right: 0; top: 218px;
    text-align: center;
    font-family: "Lato", sans-serif; font-weight: 400;
    font-size: 15px; letter-spacing: 1px;
  }
  .front-web .upper { text-transform: uppercase; }
  /* Back */
  .card-back {
    top: 560px;
    background: linear-gradient(160deg, var(--paper) 0%, var(--paper-shade) 100%);
  }
  .back-swoosh { position: absolute; inset: 0; }
  .back-band {
    position: absolute; right: 0; top: 160px; bottom: 0; width: 34px;
    background: var(--brand-blue);
  }
  .back-corner-dot {
    position: absolute; right: -14px; top: -14px;
    width: 56px; height: 56px; border-radius: 50%;
    background: var(--brand-blue);
  }
  .back-wordmark {
    position: absolute; left: 48px; top: 70px;
    display: flex; align-items: center; gap: 12px;
    color: var(--brand-blue);
  }
  .back-wordmark .wordmark-name { font-size: 28px; }
  .back-wordmark .wordmark-dot { width: 13px; height: 13px; }
  .holder {
    position: absolute; right: 70px; top: 150px; text-align: right;
  }
  .holder-name {
    font-family: "Montserrat", sans-serif; font-weight: 700;
    font-size: 22px; color: var(--brand-blue); text-transform: uppercase;
  }
  .holder-role {
    font-family: "Lato", sans-serif; font-weight: 300;
    font-size: 15px; color: var(--ink-grey); margin-top: 2px;
  }
  .divider {
    position: absolute; left: 48px; right: 70px; top: 226px;
    height: 1.5px; background: var(--brand-blue);
  }
  .contacts {
    position: absolute; left: 48px; top: 244px; list-style: none;
    font-family: "Lato", sans-serif; font-weight: 400;
    font-size: 15px; color: var(--ink-grey);
  }
  .contacts li { display: flex; align-items: center; gap: 10px; height: 24px; }
  .contacts svg { width: 15px; height: 15px; flex: none; }
</style>
</head>
<body>
<main class="canvas">

  <section class="card card-front" aria-label="Card front">
    <div class="front-wordmark">
      <span class="wordmark-dot"></span>
      <span class="wordmark-name">Tarrow Construct Works</span>
    </div>
    <p class="front-web">www.<span class="upper">tarrowconstructworks</span>.com.au</p>
  </section>

  <section class="card card-back" aria-label="Card back">
    <svg class="back-swoosh" viewBox="0 0 620 360" preserveAspectRatio="none" aria-hidden="true">
      <path d="M330 360 C 360 180, 470 60, 620 20 L620 70 C 500 110, 410 210, 390 360 Z" fill="#ffffff" opacity=".85"/>
      <path d="M300 360 C 330 200, 430 80, 600 30" fill="none" stroke="#d4d5d9" stroke-width="2"/>
    </svg>
    <div class="back-band"></div>
    <div class="back-corner-dot"></div>

    <div class="back-wordmark">
      <span class="wordmark-dot"></span>
      <span class="wordmark-name">Tarrow Construct Works</span>
    </div>

    <div class="holder">
      <p class="holder-name">Marcus Hollin</p>
      <p class="holder-role">Managing Director</p>
    </div>
    <div class="divider"></div>

    <ul class="contacts">
      <li>
        <svg viewBox="0 0 16 16" aria-hidden="true"><circle cx="8" cy="8" r="7.5" fill="none" stroke="#0255a3" stroke-width="1.2"/><path d="M5.3 4.5l1.4-.3.8 1.8-.9.7c.4.9 1.1 1.6 2 2l.7-.9 1.8.8-.3 1.4c-2.8.2-5.7-2.7-5.5-5.5z" fill="#0255a3"/></svg>
        0472 913 046
      </li>
      <li>
        <svg viewBox="0 0 16 16" aria-hidden="true"><rect x="1.5" y="3.5" width="13" height="9" rx="1" fill="#0255a3"/><path d="M1.5 4l6.5 5 6.5-5" fill="none" stroke="#fff" stroke-width="1.2"/></svg>
        admin@tarrowconstructworks.com.au
      </li>
      <li>
        <svg viewBox="0 0 16 16" aria-hidden="true"><circle cx="8" cy="8" r="7" fill="#0255a3"/><path d="M1 8h14M8 1c-3 3.5-3 10.5 0 14M8 1c3 3.5 3 10.5 0 14" fill="none" stroke="#fff" stroke-width="1"/></svg>
        www.tarrowconstructworks.com.au
      </li>
    </ul>
  </section>

</main>
</body>
</html>
```